Fall by my site ads for Facebook

I run an events and exhibition company in Singapore and we are trying to build a presence on Facebook. But my colleagues and I are not very good with web banner and Facebook ad designs so most of our postings are boring and doesn't hit the crowd. So I would like to outsource the design of a series of 3 x banner ad or Facebook posting that creates awareness and bring viewers to my website www.plumtavo.com. Our business is of a B2B nature and our clients are typically well-educated young professionals age 25 to 40 and are social media savvy. They are usually from the Marketing, PR, Communications or Media verticals and typically browse Facebook and Instagram at least once a day.

Target Market(s)

well-educated young professionals age 25 to 40 and are social media savvy. They are usually from the Marketing, PR, Communications or Media verticals and typically browse Facebook and Instagram at least once a day.

Industry/Entity Type

Events

Requirements
Must have
• Our website www.plumtavo.com

```html
<!DOCTYPE html>
<html lang="en">
<head>
<meta charset="utf-8">
<title>Concept Plan Execute</title>
<link rel="stylesheet" href="https://fonts.googleapis.com/css2?family=Montserrat:wght@300;400&display=swap">
<style>
  :root {
    --ink: #000000;
    --white: #ffffff;
    --amber: #e9a21f;
    --band-top-a: #d99a22;
    --band-top-b: #a9700c;
    --band-mid-a: #8d5c09;
    --band-mid-b: #5e3c05;
    --band-low-a: #7a5008;
    --band-low-b: #3e2803;
  }
  html, body {
    margin: 0;
    padding: 0;
    width: 1200px;
    height: 1200px;
    overflow: hidden;
    background: var(--ink);
  }
  .poster {
    display: block;
    width: 1200px;
    height: 1200px;
  }
  .headline {
    font-family: "Montserrat", sans-serif;
    font-weight: 300;
    fill: var(--white);
  }
  .brand {
    font-family: "Montserrat", sans-serif;
    font-weight: 300;
    font-size: 34px;
    fill: var(--amber);
  }
  .tagline {
    font-family: "Montserrat", sans-serif;
    font-weight: 400;
    font-size: 30px;
    fill: var(--white);
  }
  .tagline .accent { fill: var(--amber); }
  .website {
    font-family: "Montserrat", sans-serif;
    font-weight: 400;
    font-size: 26px;
    fill: var(--white);
  }
  .divider { stroke: var(--white); stroke-width: 1.5; opacity: 0.7; }
</style>
</head>
<body>
<svg class="poster" viewBox="0 0 1200 1200" xmlns="http://www.w3.org/2000/svg">
  <defs>
    <linearGradient id="band-top" x1="0" y1="0" x2="1" y2="1">
      <stop offset="0" stop-color="var(--band-top-a)"/>
      <stop offset="1" stop-color="var(--band-top-b)"/>
    </linearGradient>
    <linearGradient id="band-mid" x1="0" y1="0" x2="1" y2="1">
      <stop offset="0" stop-color="var(--band-mid-a)"/>
      <stop offset="1" stop-color="var(--band-mid-b)"/>
    </linearGradient>
    <linearGradient id="band-low" x1="0" y1="0" x2="1" y2="1">
      <stop offset="0" stop-color="var(--band-low-a)"/>
      <stop offset="1" stop-color="var(--band-low-b)"/>
    </linearGradient>
  </defs>

  <rect width="1200" height="1200" fill="var(--ink)"/>

  <rect class="photo-band" x="35" y="35" width="1128" height="339" fill="url(#band-top)"
        role="img" aria-label="Amber-toned photo of a child reading an exhibition display panel"/>
  <rect class="photo-band" x="35" y="392" width="1128" height="336" fill="url(#band-mid)"
        role="img" aria-label="Amber-toned photo of a produce exhibition booth with crates of apples and juice packs"/>
  <rect class="photo-band" x="35" y="747" width="1128" height="338" fill="url(#band-low)"
        role="img" aria-label="Amber-toned photo of a large stone sculpture at an event venue"/>

  <text class="headline" x="93" y="240" font-size="160" textLength="1011" lengthAdjust="spacingAndGlyphs">CONCEPT</text>
  <text class="headline" x="96" y="680" font-size="355" textLength="1016" lengthAdjust="spacingAndGlyphs">PLAN</text>
  <text class="headline" x="96" y="992" font-size="262" textLength="1008" lengthAdjust="spacingAndGlyphs">EXECUTE</text>

  <text class="brand" x="35" y="1160" textLength="258" lengthAdjust="spacingAndGlyphs">Lumera Studio</text>
  <line class="divider" x1="330" y1="1104" x2="330" y2="1184"/>
  <text class="tagline" x="368" y="1163">think big <tspan class="accent">win the world</tspan></text>
  <text class="website" x="1163" y="1162" text-anchor="end">www.plumtavo.com</text>
</svg>
</body>
</html>
```